Wedding Photography Infographic

I am looking for an Infographic that has multiple uses. I want it to be used in emails when I respond to client enquiries or leads, to make my business stand out, The infographic can also potentially be used on my website and obtaining backlinks by submitting it to sites.

I am looking for some originality so please take time with your entries. As soon as I get a couple of good designs I will change the contest to a guaranteed award. I have posted a contest before and I this is exactly what I did. I am diligent at responding to all designs with ratings and comments. I am happy to receive part designs that I can rate so you don't waste too much time with no idea of my reaction.

I have attached the sections of the Infographic and wording to be used. I welcome any comments. I am avoiding mentioning things like pricing or awards that can become out of date quickly. However in an ideal world I would like to be able to change wording once the design has been complete. Let me know if this possible and what format you will give me the design.

My website is velvetlantern.co.uk. Please have a look at this as my photography style may change your design approach.

I appreciate contests attract people that want to get started on the site and need a good review. I promise that the winning review will receive a good review.

Look forward to receiving some great entries.

Derek

```html
<!DOCTYPE html>
<html lang="en">
<head>
<meta charset="utf-8">
<title>Why Choose Me – Velvet Lantern Wedding Photography</title>
<link href="https://fonts.googleapis.com/css2?family=Open+Sans:wght@600;700;800&display=swap" rel="stylesheet">
<style>
  :root {
    --bg: #272727;
    --bg-edge: #1c1c1c;
    --red: #e5403a;
    --text: #c4c4c4;
    --panel: #b9b9b9;
    --panel-text: #2b2b2b;
    --rule: #bdbdbd;
  }
  html, body { margin: 0; padding: 0; overflow: hidden; background: var(--bg-edge); }
  .poster {
    position: relative;
    width: 854px;
    height: 1200px;
    overflow: hidden;
    background: radial-gradient(ellipse at 50% 45%, #2e2e2e 0%, var(--bg) 60%, var(--bg-edge) 100%);
    font-family: "Open Sans", Arial, sans-serif;
    color: var(--text);
  }
  .poster * { position: absolute; margin: 0; white-space: nowrap; }
  .poster svg { display: block; }

  /* brand */
  .brand-mark { left: 62px; top: 22px; width: 42px; height: 42px; border-radius: 50%; background: var(--text); }
  .brand-name { left: 22px; top: 76px; width: 128px; text-align: center; font-size: 10px; font-weight: 700; letter-spacing: 0.5px; }

  /* headline */
  .headline { left: 160px; top: 14px; font-size: 60px; font-weight: 800; color: var(--red); letter-spacing: 1px; line-height: 1; }
  .headline-rule { left: 160px; top: 94px; width: 660px; height: 3px; background: var(--red); }

  /* dashed dividers */
  .divider-h { height: 0; border-top: 2px dashed var(--rule); opacity: 0.75; }
  .divider-v { width: 0; border-left: 2px dashed var(--rule); opacity: 0.75; }

  .big { font-weight: 700; line-height: 1; letter-spacing: -0.5px; }

  /* experience */
  .exp-1 { left: 245px; top: 122px; font-size: 57px; }
  .exp-2 { left: 243px; top: 194px; font-size: 80px; }

  /* style panel */
  .style-panel { left: 40px; top: 305px; width: 597px; height: 115px; background: var(--panel); color: var(--panel-text); }
  .style-label-small { left: 18px; top: 27px; font-size: 15px; font-weight: 800; }
  .style-label-big { left: 16px; top: 46px; font-size: 40px; font-weight: 800; line-height: 1; }
  .style-list { left: 200px; top: 24px; list-style: none; padding: 0; font-size: 22px; font-weight: 700; line-height: 33px; }
  .style-list li { position: relative; padding-left: 28px; }
  .style-list li::before { content: "•"; position: absolute; left: 0; top: 0; }

  /* creative */
  .cef { left: 666px; top: 434px; font-weight: 700; line-height: 31px; font-size: 27px; letter-spacing: -0.5px; }
  .cef span { position: static; color: var(--red); }
  .cef-line { position: relative !important; display: block; }

  /* venues */
  .venue-1 { left: 337px; top: 431px; font-size: 36px; }
  .venue-2 { left: 336px; top: 470px; font-size: 58px; }

  /* insurance */
  .insurance { left: 23px; top: 594px; font-size: 31px; font-weight: 700; line-height: 47px; letter-spacing: -0.3px; }

  /* friendly */
  .friendly-1 { left: 508px; top: 556px; font-size: 66px; }
  .friendly-2 { left: 510px; top: 633px; font-size: 43px; }
  .friendly-3 { left: 510px; top: 685px; font-size: 34px; }

  /* retouching */
  .retouch-1 { left: 92px; top: 758px; font-size: 40px; }
  .retouch-2 { left: 90px; top: 808px; font-size: 54px; }

  /* kit */
  .kit-panel { left: 507px; top: 760px; width: 148px; height: 240px; background: var(--panel); color: var(--panel-text); }
  .kit-title { left: 8px; top: 0; font-size: 74px; font-weight: 800; line-height: 1.1; letter-spacing: -2px; }
  .kit-list { left: 10px; top: 110px; list-style: none; padding: 0; font-size: 8.5px; font-weight: 600; line-height: 11.5px; }
  .kit-list li { position: relative; padding-left: 8px; }
  .kit-list li::before { content: "•"; position: absolute; left: 0; }

  .equip { left: 678px; top: 898px; width: 140px; text-align: center; font-weight: 700; line-height: 1.15; }
  .equip-1 { position: relative !important; display: block; font-size: 25px; }
  .equip-2 { position: relative !important; display: block; font-size: 33px; }
  .equip-3 { position: relative !important; display: block; font-size: 23px; }

  /* album */
  .album { left: 145px; top: 896px; font-size: 26.5px; font-weight: 700; line-height: 37px; letter-spacing: -0.3px; }

  /* respond */
  .respond-1 { left: 245px; top: 1036px; font-size: 58px; }
  .respond-2 { left: 243px; top: 1107px; font-size: 53px; }
</style>
</head>
<body>
<main class="poster">

  <span class="brand-mark"></span>
  <p class="brand-name">VELVET LANTERN</p>

  <h1 class="headline">WHY CHOOSE ME ?</h1>
  <span class="headline-rule"></span>

  <!-- experience -->
  <svg class="icon-camera" style="left:25px;top:125px" width="200" height="146" viewBox="0 0 200 146" aria-hidden="true">
    <rect x="0" y="22" width="200" height="124" rx="10" fill="var(--red)"/>
    <rect x="28" y="4" width="62" height="30" rx="6" fill="var(--red)"/>
    <rect x="140" y="30" width="44" height="10" fill="var(--bg)"/>
    <circle cx="92" cy="88" r="44" fill="var(--bg)"/>
    <circle cx="92" cy="88" r="25" fill="var(--red)"/>
  </svg>
  <p class="big exp-1">Photographed over</p>
  <p class="big exp-2">300 weddings</p>

  <div class="divider-h" style="left:25px;top:292px;width:795px"></div>
  <div class="divider-v" style="left:654px;top:292px;height:252px"></div>

  <!-- style -->
  <section class="style-panel">
    <p class="style-label-small">PHOTOGRAPHY</p>
    <p class="style-label-big">STYLE</p>
    <ul class="style-list">
      <li>Documentary Style.</li>
      <li>Relaxed and informal posing</li>
    </ul>
  </section>

  <!-- creative -->
  <svg class="icon-envelope" style="left:672px;top:312px" width="147" height="92" viewBox="0 0 147 92" aria-hidden="true">
    <rect x="0" y="0" width="147" height="92" rx="4" fill="var(--red)"/>
    <polyline points="8,8 73,52 139,8" fill="none" stroke="var(--bg)" stroke-width="3"/>
    <line x1="73" y1="52" x2="73" y2="88" stroke="var(--bg)" stroke-width="3"/>
    <text x="73" y="34" text-anchor="middle" font-family="Open Sans, sans-serif" font-weight="700" font-size="18" fill="var(--bg)">C</text>
    <text x="38" y="78" text-anchor="middle" font-family="Open Sans, sans-serif" font-weight="700" font-size="18" fill="var(--bg)">F</text>
    <text x="110" y="78" text-anchor="middle" font-family="Open Sans, sans-serif" font-weight="700" font-size="18" fill="var(--bg)">E</text>
  </svg>
  <p class="cef">
    <span class="cef-line" style="font-size:30px"><span>C</span>reative,</span>
    <span class="cef-line" style="font-size:24px"><span>E</span>motive and</span>
    <span class="cef-line" style="font-size:24px"><span>F</span>un images</span>
  </p>

  <!-- insurance -->
  <svg class="icon-dollar" style="left:25px;top:437px" width="200" height="143" viewBox="0 0 200 143" aria-hidden="true">
    <rect width="200" height="143" rx="8" fill="var(--red)"/>
    <text x="100" y="96" text-anchor="middle" font-family="Open Sans, sans-serif" font-weight="800" font-size="70" fill="var(--bg)">$</text>
  </svg>
  <p class="insurance">Professional<br>Indemnity<br>Insurance</p>

  <div class="divider-v" style="left:236px;top:430px;height:296px"></div>

  <!-- venues -->
  <svg class="icon-pin" style="left:250px;top:440px" width="62" height="88" viewBox="0 0 62 88" aria-hidden="true">
    <path d="M31 88 C22 70 0 50 0 31 A31 31 0 0 1 62 31 C62 50 40 70 31 88 Z" fill="var(--red)"/>
    <circle cx="31" cy="31" r="13" fill="none" stroke="var(--bg)" stroke-width="5"/>
  </svg>
  <p class="big venue-1">Great knowledge</p>
  <p class="big venue-2">of venues</p>

  <div class="divider-h" style="left:237px;top:543px;width:583px"></div>

  <!-- friendly -->
  <svg class="icon-smile" style="left:245px;top:557px" width="243" height="173" viewBox="0 0 243 173" aria-hidden="true">
    <rect width="243" height="173" rx="12" fill="var(--red)"/>
    <circle cx="94" cy="38" r="6" fill="var(--bg)"/>
    <circle cx="150" cy="38" r="6" fill="var(--bg)"/>
    <path d="M48 78 Q122 196 196 78" fill="none" stroke="var(--bg)" stroke-width="4"/>
  </svg>
  <p class="big friendly-1">Friendly</p>
  <p class="big friendly-2">and engaging</p>
  <p class="big friendly-3">personal service</p>

  <div class="divider-h" style="left:25px;top:742px;width:795px"></div>

  <!-- retouching -->
  <svg class="icon-mouse" style="left:25px;top:758px" width="50" height="102" viewBox="0 0 50 102" aria-hidden="true">
    <path d="M22 10 Q22 0 32 2" fill="none" stroke="var(--red)" stroke-width="4"/>
    <path d="M2 36 A23 23 0 0 1 23 18 L23 44 L2 44 Z" fill="var(--red)"/>
    <path d="M27 18 A23 23 0 0 1 48 36 L48 44 L27 44 Z" fill="var(--red)"/>
    <path d="M2 48 L48 48 L48 78 A23 23 0 0 1 2 78 Z" fill="var(--red)"/>
  </svg>
  <p class="big retouch-1">Digital retouching</p>
  <p class="big retouch-2">on all images</p>

  <!-- kit -->
  <section class="kit-panel">
    <p class="kit-title">KIT</p>
    <ul class="kit-list">
      <li>Kestrel K3 and backup</li>
      <li>24mm f1.4 Kestrel prime</li>
      <li>50 mm f1.4 Kestrel prime</li>
      <li>70-200 mm Kestrel f2.8</li>
      <li>Macro,fisheye and wide<br>angle lenses</li>
      <li>KF800 flash and Lumora<br>Pack flash system</li>
    </ul>
  </section>

  <svg class="icon-tools" style="left:680px;top:760px" width="137" height="122" viewBox="0 0 137 122" aria-hidden="true">
    <g fill="var(--red)">
      <path d="M6 20 A20 20 0 0 1 34 2 L24 14 L30 24 L42 22 L50 10 A20 20 0 0 1 36 40 L112 116 A8 8 0 0 1 100 122 L26 46 A20 20 0 0 1 6 20 Z"/>
      <path d="M96 6 L128 6 L137 20 L124 30 L110 20 L104 26 L26 112 A8 8 0 0 1 14 102 L92 22 L86 16 Z"/>
    </g>
  </svg>
  <p class="equip">
    <span class="equip-1">Expensive</span>
    <span class="equip-2">Quality</span>
    <span class="equip-3">Equipment</span>
  </p>

  <div class="divider-h" style="left:25px;top:880px;width:465px"></div>

  <!-- album -->
  <svg class="icon-disc" style="left:25px;top:903px" width="82" height="82" viewBox="0 0 82 82" aria-hidden="true">
    <circle cx="41" cy="41" r="41" fill="var(--red)"/>
    <circle cx="41" cy="41" r="11" fill="var(--bg)"/>
    <circle cx="41" cy="41" r="4" fill="var(--red)"/>
    <path d="M33 48 L12 68 M29 44 L8 62" stroke="var(--bg)" stroke-width="4"/>
  </svg>
  <p class="album">Album proofing software<br>making amendments<br>an efficient process</p>

  <div class="divider-h" style="left:25px;top:1018px;width:795px"></div>

  <!-- respond -->
  <svg class="icon-reply" style="left:25px;top:1033px" width="187" height="147" viewBox="0 0 187 147" aria-hidden="true">
    <rect width="187" height="147" rx="8" fill="var(--red)"/>
    <path d="M52 72 L86 44 L86 62 Q128 62 130 104 Q116 82 86 82 L86 100 Z" fill="var(--bg)"/>
  </svg>
  <p class="big respond-1">Always respond to</p>
  <p class="big respond-2">special requirements</p>

</main>
</body>
</html>
```